Reliable and clean label for a natural product!

We would like to have a label design for our CBD SOFT GEL CAPSULES . We are a business family and believe in the power of natural healing. In this label we would like to show a reliable, natural and feminine product mainly.

Font styles to use
Serif
Sans Serif

Colors

Designer to choose colors to be used in the design.

```html
<!DOCTYPE html>
<html lang="en">
<head>
<meta charset="UTF-8">
<title>Solenne Botanics – CBD Soft Gel Capsules Label</title>
<link rel="stylesheet" href="https://fonts.googleapis.com/css2?family=Montserrat:wght@400;500;600;700;800&display=swap">
<style>
  :root {
    --backdrop: #d4d5dc;
    --label-white: #ffffff;
    --brand-purple: #6b5a9f;
    --teal-light: #6fd0c2;
    --teal: #1f9f90;
    --blue: #1e98d4;
    --lavender: #a69cc8;
    --purple: #6d519a;
    --band-teal: #4cb8a8;
    --text-white: #ffffff;
    --pill-text: #7a5fae;
  }
  html, body {
    margin: 0;
    padding: 0;
    width: 1200px;
    height: 1200px;
    overflow: hidden;
    background: var(--backdrop);
    font-family: "Montserrat", sans-serif;
  }
  .canvas {
    position: relative;
    width: 1200px;
    height: 1200px;
  }
  .label {
    position: absolute;
    left: 190px;
    top: 105px;
    width: 820px;
    height: 990px;
    background: var(--label-white);
    box-shadow: 0 12px 40px rgba(60, 60, 80, 0.15);
    overflow: hidden;
  }
  .brand-area {
    height: 282px;
    display: flex;
    align-items: center;
    justify-content: center;
    gap: 18px;
  }
  .brand-dot {
    width: 34px;
    height: 34px;
    border-radius: 50%;
    border: 3px solid var(--brand-purple);
    box-sizing: border-box;
  }
  .brand-name {
    font-weight: 500;
    font-size: 50px;
    letter-spacing: 1px;
    color: var(--brand-purple);
    text-transform: uppercase;
  }
  .hero-band {
    position: relative;
    height: 627px;
    background: linear-gradient(180deg,
      var(--teal-light) 0%,
      var(--teal) 14%,
      var(--blue) 40%,
      #3a8fc4 58%,
      var(--lavender) 72%,
      var(--purple) 100%);
    color: var(--text-white);
    text-align: center;
  }
  .hero-band > * {
    position: absolute;
    left: 0;
    right: 0;
    margin: 0;
  }
  .tagline {
    top: 28px;
    font-weight: 700;
    font-size: 36px;
    line-height: 40px;
    letter-spacing: 0.5px;
  }
  .tagline-rule {
    top: 93px;
    left: 130px;
    right: 130px;
    height: 2px;
    background: rgba(255, 255, 255, 0.3);
  }
  .product-title {
    top: 107px;
    font-weight: 500;
    font-size: 74px;
    line-height: 72px;
    letter-spacing: 1px;
  }
  .product-title span { display: block; }
  .product-cbd {
    top: 248px;
    font-weight: 800;
    font-size: 182px;
    line-height: 160px;
    letter-spacing: 4px;
  }
  .pill-row {
    top: 435px;
    display: flex;
    justify-content: center;
  }
  .pill {
    height: 62px;
    width: 518px;
    box-sizing: border-box;
    background: rgba(255, 255, 255, 0.92);
    border-radius: 31px;
    color: var(--pill-text);
    font-weight: 500;
    font-size: 31px;
    line-height: 62px;
  }
  .spec {
    top: 522px;
    font-weight: 600;
    font-size: 34px;
    line-height: 42px;
  }
  .count-band {
    height: 81px;
    background: var(--band-teal);
    color: var(--text-white);
    display: flex;
    align-items: center;
    justify-content: center;
    font-weight: 500;
    font-size: 38px;
    letter-spacing: 1px;
  }
</style>
</head>
<body>
<div class="canvas">
  <section class="label">
    <header class="brand-area">
      <div class="brand-dot"></div>
      <div class="brand-name">Solenne Botanics</div>
    </header>
    <div class="hero-band">
      <div class="tagline">RESTORATIVE SUPPLEMENT</div>
      <div class="tagline-rule"></div>
      <h1 class="product-title">
        <span>CAPSULAS</span>
        <span>ACEITE DE</span>
      </h1>
      <div class="product-cbd">CBD</div>
      <div class="pill-row"><div class="pill">Hemp Oil Extract Capsules</div></div>
      <div class="spec">Full Spectrum<br>25 mg CBD per capsule</div>
    </div>
    <footer class="count-band">30 CAPSULES</footer>
  </section>
</div>
</body>
</html>
```